Front & Back Book Cover Design

Title:
THE QUIET LANDLORD: How to Grow Comfort and Capital Through Property You Merely Guide
Author:
Wes T. Marlund
Design Philosophy:
A modern, minimalist-luxury aesthetic that feels visionary and intelligent — positioned between business innovation (The Nimble Venture), modern finance (The Temperament of Wealth), and timeless real estate insight (Bold Uncle Meek Uncle).
Think: clean, bold, and idea-driven — a visual reflection of the book’s central concept: wealth through clarity, not clutter.
Back Cover:
To include book description along with author photo and bio
Files:
PNG, PDF, EPUB

```html
<!DOCTYPE html>
<html lang="en">
<head>
<meta charset="utf-8">
<title>The Quiet Landlord — Book Cover</title>
<link href="https://fonts.googleapis.com/css2?family=Bebas+Neue&family=Nunito+Sans:ital,wght@0,300;0,400;0,700;0,800;1,300&display=swap" rel="stylesheet">
<style>
  :root {
    --stage: #ebebeb;
    --cover-top: #c9e3ed;
    --cover-mid: #c3d9e4;
    --cover-bottom: #acc1d2;
    --flap-top: #b9dbe9;
    --flap-bottom: #a9c3d6;
    --title-blue: #0e9fd4;
    --title-deep: #1680bd;
    --author-blue: #1b9cd6;
    --text-white: #f4f9fc;
    --box-fill: rgba(220, 238, 246, 0.75);
    --shadow: rgba(40, 60, 80, 0.28);
  }
  * { box-sizing: border-box; margin: 0; padding: 0; }
  html, body { width: 1003px; height: 1200px; overflow: hidden; }
  body {
    background: var(--stage);
    font-family: "Nunito Sans", sans-serif;
    position: relative;
  }
  .title {
    font-family: "Bebas Neue", sans-serif;
    background: linear-gradient(180deg, var(--title-blue), var(--title-deep));
    -webkit-background-clip: text;
    background-clip: text;
    color: transparent;
    line-height: 0.86;
    letter-spacing: 0.5px;
  }
  .author-name {
    font-family: "Bebas Neue", sans-serif;
    color: var(--author-blue);
    letter-spacing: 0.3px;
  }
  .cover-surface {
    background: linear-gradient(180deg, var(--cover-top) 0%, var(--cover-mid) 50%, var(--cover-bottom) 100%);
  }
  .symbol-art {
    position: absolute;
    left: 50%;
    transform: translateX(-50%);
    border-radius: 40px;
    background: radial-gradient(ellipse at 45% 45%, #2b9ad0 0%, #3aa3d6 35%, rgba(100,170,210,0.35) 70%, rgba(160,200,220,0) 100%);
  }
  .symbol-shadow {
    position: absolute;
    left: 50%;
    transform: translateX(-50%);
    border-radius: 50%;
    background: radial-gradient(ellipse, rgba(60,120,175,0.55), rgba(60,120,175,0) 70%);
  }

  /* Front cover */
  .front-cover {
    position: absolute;
    left: 336px; top: 108px;
    width: 330px; height: 436px;
    box-shadow: 6px 8px 16px var(--shadow);
  }
  .front-cover .title { position: absolute; left: 24px; top: 26px; font-size: 68px; }
  .front-cover .symbol-art { top: 158px; width: 100px; height: 210px; }
  .front-cover .symbol-shadow { top: 370px; width: 120px; height: 22px; }
  .front-cover .author-name { position: absolute; width: 100%; text-align: center; bottom: 26px; font-size: 20px; }

  /* Full jacket */
  .jacket {
    position: absolute;
    left: 74px; top: 673px;
    width: 856px; height: 407px;
    display: flex;
    box-shadow: 4px 8px 14px var(--shadow);
  }
  .panel { position: relative; height: 100%; }
  .flap {
    width: 136px;
    background: linear-gradient(180deg, var(--flap-top), var(--flap-bottom));
  }
  .flap-front .title { position: absolute; left: 11px; top: 30px; font-size: 26.5px; }
  .flap-front .author-name { position: absolute; left: 11px; top: 84px; font-size: 9px; }
  .glass-art {
    position: absolute; left: 0; top: 145px; width: 134px; height: 262px;
    background: linear-gradient(160deg, rgba(230,245,252,0.9), rgba(190,220,235,0.6) 45%, rgba(215,235,245,0.85));
    border-top-right-radius: 120px 150px;
  }

  .back { width: 270px; padding: 28px 15px 0 22px; }
  .back-heading { font-weight: 800; font-size: 7.2px; color: var(--title-blue); letter-spacing: 0.2px; }
  .back-subtitle { font-style: italic; font-weight: 300; font-size: 9px; line-height: 1.25; color: var(--text-white); margin-top: 2px; }
  .back-byline { font-size: 6.8px; color: var(--text-white); font-weight: 300; }
  .back-hook { font-size: 7.2px; color: var(--title-deep); margin-top: 8px; line-height: 1.3; }
  .back-body { font-size: 6.9px; font-weight: 300; color: var(--text-white); line-height: 1.32; margin-top: 8px; }
  .benefits {
    list-style: none;
    background: var(--box-fill);
    border-radius: 5px;
    box-shadow: 0 2px 5px rgba(60,100,130,0.2);
    padding: 7px 8px 8px 7px;
    margin: 12px 0 16px -5px;
    width: 240px;
  }
  .benefits li { font-size: 5.3px; font-weight: 700; color: var(--title-deep); line-height: 1.25; margin-bottom: 6px; padding-left: 4px; text-indent: -4px; }
  .benefits li:last-child { margin-bottom: 0; }
  .back-close { font-size: 7px; font-weight: 800; color: var(--text-white); margin-top: 9px; }

  .spine {
    width: 42px;
    background: linear-gradient(180deg, #cfe4ee, var(--cover-bottom));
    border-left: 1px solid rgba(255,255,255,0.4);
    border-right: 1px solid rgba(255,255,255,0.4);
  }
  .spine-author {
    position: absolute; top: 20px; left: 14px;
    writing-mode: vertical-rl;
    font-size: 6.5px; font-weight: 700; color: var(--text-white);
  }
  .spine-title {
    position: absolute; bottom: 14px; left: 9px;
    writing-mode: vertical-rl; transform: rotate(180deg);
    font-family: "Bebas Neue", sans-serif; font-size: 25px; color: var(--text-white); letter-spacing: 0.3px;
  }

  .front { width: 272px; }
  .front .title { position: absolute; left: 11px; top: 18px; font-size: 58px; }
  .front .symbol-art { top: 128px; width: 96px; height: 200px; }
  .front .symbol-shadow { top: 330px; width: 120px; height: 22px; }
  .front .author-name { position: absolute; width: 100%; text-align: center; bottom: 10px; font-size: 17px; }

  .flap-back .author-photo {
    position: absolute; left: 29px; top: 23px; width: 77px; height: 98px;
    background: linear-gradient(180deg, #8a8580, #4d4a47 60%, #5e5954);
    border: 1px solid #3c3a38;
  }
  .flap-back .author-name { position: absolute; right: 29px; top: 126px; font-size: 8px; }
  .author-bio {
    position: absolute; left: 19px; top: 166px; width: 108px;
    font-size: 5.4px; font-weight: 300; color: var(--text-white); line-height: 1.38;
  }
</style>
</head>
<body>

<section class="front-cover cover-surface">
  <h1 class="title">The Quiet<br>Landlord</h1>
  <div class="symbol-art" role="img" aria-label="Large three-dimensional blue dollar sign floating above the cover"></div>
  <div class="symbol-shadow"></div>
  <p class="author-name">Wes T. Marlund</p>
</section>

<section class="jacket">
  <div class="panel flap flap-front">
    <h2 class="title">The Quiet<br>Landlord</h2>
    <p class="author-name">Wes T. Marlund</p>
    <div class="glass-art" role="img" aria-label="Translucent flowing glass wave in pale blue"></div>
  </div>

  <div class="panel back cover-surface">
    <p class="back-heading">THE QUIET LANDLORD</p>
    <p class="back-subtitle">How to Grow Comfort and Capital Through<br>Property You Merely Guide</p>
    <p class="back-byline">by Wes T. Marlund</p>
    <p class="back-hook">What if the smartest real estate investors in the world don’t actually own anything?</p>
    <p class="back-body">In a world where leverage has replaced labor and access has replaced assets, The Quiet Landlord reveals how a new generation of entrepreneurs is building wealth without deeds, mortgages, or massive capital.</p>
    <p class="back-body">Wes T. Marlund exposes the hidden playbook behind modern real estate wealth — not through ownership, but through control, creativity, and influence.</p>
    <p class="back-body">You’ll discover how to:</p>
    <ul class="benefits">
      <li>• Profit from properties you never buy through partnerships, performance models, and control agreements.</li>
      <li>• Monetize your skills, systems, and relationships just like institutional investors do. Build digital real estate — brands, websites, and lead funnels that pay like rentals.</li>
      <li>• Create recurring income through master leases, management contracts, and service-based equity.</li>
      <li>• Design your freedom formula — where wealth is measured in time, not titles.</li>
    </ul>
    <p class="back-body">Packed with frameworks, examples, and the mindset of modern deal-makers, The Quiet Landlord is a blueprint for the future of wealth creation — one built on access, not assets.</p>
    <p class="back-body">Because in the new economy, the most powerful investors don’t own real estate. They own opportunity.</p>
    <p class="back-close">And now, you can too.</p>
  </div>

  <div class="panel spine">
    <p class="spine-author">Wes T. Marlund</p>
    <p class="spine-title">The Quiet Landlord</p>
  </div>

  <div class="panel front cover-surface">
    <h2 class="title">The Quiet<br>Landlord</h2>
    <div class="symbol-art" role="img" aria-label="Large three-dimensional blue dollar sign floating above the cover"></div>
    <div class="symbol-shadow"></div>
    <p class="author-name">Wes T. Marlund</p>
  </div>

  <div class="panel flap flap-back">
    <div class="author-photo" role="img" aria-label="Portrait of the author in a dark blazer in a modern office"></div>
    <p class="author-name">Wes T. Marlund</p>
    <p class="author-bio">Wes T. Marlund is a real estate entrepreneur and owner of Halvard Studio in Las Vegas, NV and Keystone Summit Realty in Ventura, California. Combining design, development, and deal strategy, he’s helped agents, investors, and entrepreneurs build freedom through systems — not stuff. The Quiet Landlord is his definitive guide to building wealth through creative control.</p>
  </div>
</section>

</body>
</html>
```